steuerberater flyer
Zielgruppe
wir möchten weitere steuerberater hinzugewinnen für diese wir als freie mitarbeiter tätig werden!
Aufgabenstellung
es soll ein einfacher dinalang flyer werden, evtl. alle infos auf der vorderseite nur......oder aufgeteilt, das überlasen wir ihnen, so das vielleicht nur die erste seite erstmal ein eyecatcher ist! DEr ist txt ist anbei, diesen anschreiben soll quasi erstetzt werden, der flyer soll natürlich nicht personalisiert sein.

```html
<!DOCTYPE html>
<html lang="de">
<head>
<meta charset="utf-8">
<title>Kontenwerk GmbH – Flyer</title>
<link href="https://fonts.googleapis.com/css2?family=Quicksand:wght@400;500;600;700&display=swap" rel="stylesheet">
<style>
  :root{
    --stage:#8a8a8a;
    --paper:#ffffff;
    --brand:#617cc0;
    --brand-light:#8fa0d8;
    --ink-soft:#6b6b6b;
    --star:#a8b2cf;
    --check:#c8d2ee;
    --photo-a:#eceef0;
    --photo-b:#c9cbcd;
    --photo-c:#b08a66;
  }
  *{box-sizing:border-box;margin:0;padding:0}
  html,body{width:1198px;height:1200px;overflow:hidden}
  body{background:var(--stage);font-family:"Quicksand",sans-serif;position:relative}

  .flyer{position:absolute;top:148px;width:452px;height:904px;background:var(--paper);overflow:hidden}
  .flyer--front{left:125px}
  .flyer--back{left:639px}

  /* Front */
  .brand-head{position:absolute;top:0;left:0;right:0;height:189px;display:flex;flex-direction:column;align-items:center;justify-content:center;gap:12px}
  .brand-mark{width:30px;height:30px;background:var(--brand);border-radius:3px}
  .brand-name{color:var(--brand);font-weight:500;font-size:25px;letter-spacing:1px}
  .front-photo{position:absolute;top:189px;left:0;width:100%;height:295px;
    background:linear-gradient(180deg,var(--photo-a) 0%,#dfe1e3 55%,var(--photo-b) 80%,var(--photo-c) 100%)}
  .front-panel{position:absolute;top:484px;left:0;right:0;bottom:0;background:var(--brand);color:#fff}
  .front-title{position:absolute;top:87px;left:35px;font-size:27px;font-weight:600;line-height:33px;letter-spacing:.3px}
  .qualities{position:absolute;top:253px;left:35px;display:grid;grid-template-columns:185px auto}
  .qualities ul{list-style:none}
  .qualities li{font-size:20px;line-height:24px;display:flex;align-items:center;gap:7px}
  .qualities svg{width:14px;height:14px;flex:none}

  /* Back */
  .quote-band{position:absolute;top:0;left:0;right:0;height:140px;background:var(--brand-light);color:#fff}
  .quote-mark{position:absolute;top:30px;left:52px;width:30px;height:28px}
  .quote-text{position:absolute;top:63px;left:52px;right:20px;font-size:20px;line-height:25px}
  .back-photo{position:absolute;top:140px;left:0;width:100%;height:225px;
    background:linear-gradient(90deg,#d9e6f2 0%,#f2f2f2 30%,#e8e8e8 70%,#2c2c2c 100%)}
  .back-body{position:absolute;top:394px;left:38px;right:38px;color:var(--ink-soft);font-size:15px;line-height:18.3px}
  .back-body p{margin-bottom:18px}
  .back-body .justify{text-align:justify}
  .services{list-style:none;margin-bottom:18px}
  .services li{display:flex;gap:5px}
  .services svg{width:15px;height:15px;flex:none;margin-top:1px}
  .call{color:var(--brand)}
  .back-footer{position:absolute;top:748px;left:0;right:0;bottom:0;background:var(--brand);color:#fff;font-size:15px}
  .footer-company{position:absolute;top:38px;left:47px;font-weight:600}
  .footer-address{position:absolute;top:87px;left:47px;line-height:24.5px}
  .footer-pin{position:absolute;top:89px;left:26px;width:13px;height:18px}
  .footer-contact{position:absolute;top:38px;left:223px;list-style:none;line-height:24.5px}
  .footer-contact li{display:flex;align-items:center;gap:10px}
  .footer-contact svg{width:16px;height:16px;flex:none}
</style>
</head>
<body>

<section class="flyer flyer--front">
  <header class="brand-head">
    <span class="brand-mark"></span>
    <span class="brand-name">KONTENWERK GmbH</span>
  </header>
  <div class="front-photo" role="img" aria-label="Foto: aufgeschlagener Aktenordner mit Klarsichthüllen vor einer Reihe weißer Ordner"></div>
  <div class="front-panel">
    <h1 class="front-title">BEWERBUNG ALS<br>FREIER MITARBEITER</h1>
    <div class="qualities">
      <ul>
        <li><svg viewBox="0 0 14 14"><path d="M1 7l4 4 8-9" fill="none" stroke="var(--check)" stroke-width="2.5"/></svg>fachkundig</li>
        <li><svg viewBox="0 0 14 14"><path d="M1 7l4 4 8-9" fill="none" stroke="var(--check)" stroke-width="2.5"/></svg>freundlich</li>
        <li><svg viewBox="0 0 14 14"><path d="M1 7l4 4 8-9" fill="none" stroke="var(--check)" stroke-width="2.5"/></svg>zuverlässig</li>
      </ul>
      <ul>
        <li><svg viewBox="0 0 14 14"><path d="M1 7l4 4 8-9" fill="none" stroke="var(--check)" stroke-width="2.5"/></svg>preiswert</li>
        <li><svg viewBox="0 0 14 14"><path d="M1 7l4 4 8-9" fill="none" stroke="var(--check)" stroke-width="2.5"/></svg>flexibel</li>
        <li><svg viewBox="0 0 14 14"><path d="M1 7l4 4 8-9" fill="none" stroke="var(--check)" stroke-width="2.5"/></svg>qualifiziert</li>
      </ul>
    </div>
  </div>
</section>

<section class="flyer flyer--back">
  <div class="quote-band">
    <svg class="quote-mark" viewBox="0 0 30 28"><path d="M1 0h11v12l-5 16H1l4-14H1z M17 0h12v12l-5 16h-6l4-14h-5z" fill="#fff"/></svg>
    <p class="quote-text">Suchen Sie einen flexiblen und qualifi-<br>zierten Mitarbeiter für Ihre Kanzlei?</p>
  </div>
  <div class="back-photo" role="img" aria-label="Foto: zwei Hände übergeben einen weißen Aktenordner"></div>
  <div class="back-body">
    <p>Im Rahmen der nach § 17 BOStB definierten Zusam-<br>menarbeit zwischen Buchhalter und Steuerberater<br>übernehmen wir gerne die folgenden komplexen Auf-<br>gaben für Sie:</p>
    <ul class="services">
      <li><svg viewBox="0 0 20 20"><path d="M10 1l2.6 6 6.4.5-4.9 4.2 1.5 6.3L10 14.6 4.4 18l1.5-6.3L1 7.5 7.4 7z" fill="var(--star)"/></svg>Buchhaltung</li>
      <li><svg viewBox="0 0 20 20"><path d="M10 1l2.6 6 6.4.5-4.9 4.2 1.5 6.3L10 14.6 4.4 18l1.5-6.3L1 7.5 7.4 7z" fill="var(--star)"/></svg>Lohnbuchhaltung</li>
      <li><svg viewBox="0 0 20 20"><path d="M10 1l2.6 6 6.4.5-4.9 4.2 1.5 6.3L10 14.6 4.4 18l1.5-6.3L1 7.5 7.4 7z" fill="var(--star)"/></svg><span>Vorbereitung der Jahresabschlüsse und<br>&nbsp;Steuererklärungen</span></li>
    </ul>
    <p>Wir sind bereits seit über 15 Jahren für verschiedene<br>Steuerberater tätig. Gerne würden wir unsere<br>Erfahrung und Kompetenz auch Ihnen und Ihrer Kanz-<br>lei in freier Mitarbeit nach § 17 BOStB zur Verfügung<br>stellen.</p>
    <p class="call">Setzen Sie sich mit uns in Verbindung!<br>Wir freuen uns auf Sie!</p>
  </div>
  <footer class="back-footer">
    <div class="footer-company">Kontenwerk GmbH</div>
    <svg class="footer-pin" viewBox="0 0 13 18"><path d="M6.5 0A6.5 6.5 0 0 0 0 6.5C0 11 6.5 18 6.5 18S13 11 13 6.5A6.5 6.5 0 0 0 6.5 0z" fill="#fff"/><circle cx="6.5" cy="6.5" r="2.4" fill="var(--brand)"/></svg>
    <div class="footer-address">Lindenweg 27<br>54321 Feldhausen</div>
    <ul class="footer-contact">
      <li><svg viewBox="0 0 16 16"><rect x="4" y="0" width="8" height="16" rx="1.5" fill="#fff"/><rect x="5.5" y="2" width="5" height="10" fill="var(--brand)"/></svg>0481 327 640</li>
      <li><svg viewBox="0 0 16 16"><rect x="4" y="1" width="8" height="5" fill="#fff"/><rect x="0" y="6" width="16" height="7" rx="1" fill="#fff"/><rect x="3" y="14" width="10" height="2" fill="#fff"/></svg>0481 327 641</li>
      <li><svg viewBox="0 0 16 16"><rect x="0" y="3" width="16" height="10" fill="#fff"/><path d="M0 3l8 6 8-6" fill="none" stroke="var(--brand)" stroke-width="1.3"/></svg>info@kontenwerk.de</li>
      <li><svg viewBox="0 0 16 16"><circle cx="8" cy="8" r="7.5" fill="#fff"/><path d="M8 .5v15M.5 8h15M8 .5c-4 4-4 11 0 15M8 .5c4 4 4 11 0 15" fill="none" stroke="var(--brand)" stroke-width="1"/></svg>www.kontenwerk.de</li>
    </ul>
  </footer>
</section>

</body>
</html>
```